Business card design for sports medicine and athlete care clinic.

We need a bold, solid business card design for our practitioners to stand out. We treat overuse & sports-related injuries and provide post-operative rehabilitation. Our specialisations include chronic conditions, men’s health, nutrition & musculoskeletal disorders (MSDs). All brand collateral in terms of fonts, logo and colour palette to be provided.

Target Market(s)

Athletes (professional and amateur), sportspeople, predominantly male

Industry/Entity Type

Health And Wellness

Contact Information for Business Card

The front of the card should be white with dark blue text the back dark blue with white text. The logo should be top-left. The business name should be horizontal and right of the logo. The tagline should be directly below centred on the back of the card (see top-banner.png and bottom-banner.png)

Font styles to use
Sans Serif

Colors
0355a3
0293ce
3176b5
ffffff
85acd3

Requirements
Nice to have
• Diagonal and/or horizontal line elements between logo and practitioner details and/or bottom corner of card (see slide.png and tag-bg.png).

```html
<!DOCTYPE html>
<html lang="en">
<head>
<meta charset="utf-8">
<title>Kinetic Harbour – Business Card</title>
<link rel="stylesheet" href="https://fonts.googleapis.com/css2?family=Montserrat:wght@400;500;700;800&display=swap">
<style>
  :root {
    --navy: #020b52;
    --navy-mid: #0a1a7a;
    --brand-blue: #0355a3;
    --sky: #0293ce;
    --sky-light: #29a8e8;
    --steel: #3176b5;
    --mist: #85acd3;
    --charcoal: #3c3c3e;
    --white: #ffffff;
    --backdrop: #d4d5d7;
  }
  * { box-sizing: border-box; margin: 0; padding: 0; }
  html, body { width: 1200px; height: 800px; overflow: hidden; }
  body {
    background: var(--backdrop);
    font-family: "Montserrat", sans-serif;
    display: flex;
    align-items: center;
    justify-content: center;
    gap: 40px;
  }
  .card {
    position: relative;
    width: 560px;
    height: 320px;
    border-radius: 18px;
    overflow: hidden;
    box-shadow: 0 10px 24px rgba(0,0,0,0.25);
  }

  /* Front */
  .card-front { background: var(--navy); }
  .front-bands { position: absolute; inset: 0; width: 100%; height: 100%; }
  .brand {
    position: absolute; top: 34px; left: 30px;
    display: flex; align-items: center; gap: 10px;
  }
  .brand-mark {
    width: 30px; height: 30px; border-radius: 50%;
    background: var(--sky);
    flex: none;
  }
  .brand-name {
    font-weight: 800; font-size: 22px; color: var(--navy); letter-spacing: 0.2px;
    white-space: nowrap;
  }
  .brand-tagline {
    position: absolute; top: 72px; left: 70px;
    font-weight: 700; font-size: 10.5px; color: var(--sky);
    white-space: nowrap;
  }
  .practitioner { position: absolute; top: 128px; left: 70px; color: var(--navy); }
  .practitioner-name { font-weight: 800; font-size: 22px; white-space: nowrap; }
  .practitioner-role { font-weight: 400; font-size: 14px; margin-top: 2px; }

  .contact {
    position: absolute; right: 24px; top: 74px;
    width: 205px;
    color: var(--white); font-size: 11px; font-weight: 400;
    text-align: right; line-height: 1.65;
  }
  .contact-line {
    display: flex; align-items: center; justify-content: flex-end; gap: 6px;
    white-space: nowrap;
  }
  .contact-gap { height: 12px; }
  .contact-icon { width: 11px; height: 11px; flex: none; }
  .social-dot { width: 10px; height: 10px; border-radius: 50%; background: var(--white); flex: none; }

  /* Back */
  .card-back {
    background: radial-gradient(ellipse at 55% 40%, var(--navy-mid) 0%, var(--navy) 70%);
  }
  .runner-art {
    position: absolute; left: 50%; top: 40px;
    width: 170px; height: 190px; transform: translateX(-50%);
    border-radius: 40% 50% 30% 40%;
    background: linear-gradient(150deg, var(--sky-light) 0%, var(--brand-blue) 60%, var(--mist) 100%);
    opacity: 0.9;
  }
  .back-tagline {
    position: absolute; left: 0; right: 0; bottom: 50px;
    text-align: center; color: var(--white);
    font-size: 15px; font-weight: 500; letter-spacing: 0.3px;
  }
</style>
</head>
<body>

  <section class="card card-front" aria-label="Business card front">
    <svg class="front-bands" viewBox="0 0 560 320" aria-hidden="true">
      <polygon points="0,0 240,0 290,50 290,320 0,320" fill="var(--white)"/>
      <polygon points="240,0 290,50 290,320 306,320 306,44 258,0" fill="var(--sky-light)"/>
      <polygon points="258,0 306,44 306,320 320,320 320,40 274,0" fill="var(--charcoal)"/>
      <polygon points="274,0 320,40 320,320 324,320 324,38 279,0" fill="var(--white)"/>
      <polygon points="290,50 306,44 306,320 290,320" fill="var(--brand-blue)" opacity="0.5"/>
    </svg>

    <div class="brand">
      <span class="brand-mark"></span>
      <span class="brand-name">Kinetic Harbour</span>
    </div>
    <p class="brand-tagline">Sports medicine and athlete care</p>

    <div class="practitioner">
      <p class="practitioner-name">Daniel Rowe</p>
      <p class="practitioner-role">President</p>
    </div>

    <div class="contact">
      <p class="contact-line">412 Juniper Road</p>
      <p class="contact-line">Halden, Oregon 90215</p>
      <p class="contact-line">
        <svg class="contact-icon" viewBox="0 0 24 24"><path fill="var(--white)" d="M6.6 10.8a15 15 0 0 0 6.6 6.6l2.2-2.2a1 1 0 0 1 1-.25 11.4 11.4 0 0 0 3.6.6 1 1 0 0 1 1 1V20a1 1 0 0 1-1 1A17 17 0 0 1 3 4a1 1 0 0 1 1-1h3.5a1 1 0 0 1 1 1c0 1.25.2 2.45.6 3.6a1 1 0 0 1-.25 1z"/></svg>
        555-018-4420
      </p>
      <div class="contact-gap"></div>
      <p class="contact-line">
        <svg class="contact-icon" viewBox="0 0 24 24"><rect x="2" y="5" width="20" height="14" rx="2" fill="var(--white)"/><path d="M3 6l9 7 9-7" stroke="var(--navy)" stroke-width="2" fill="none"/></svg>
        hello@kineticharbour.example
      </p>
      <p class="contact-line">
        <svg class="contact-icon" viewBox="0 0 24 24"><circle cx="12" cy="12" r="9" stroke="var(--white)" stroke-width="2" fill="none"/><path d="M3 12h18M12 3c3 3 3 15 0 18M12 3c-3 3-3 15 0 18" stroke="var(--white)" stroke-width="1.5" fill="none"/></svg>
        www.kineticharbour.example
      </p>
      <p class="contact-line">
        <span class="social-dot"></span>
        KineticHarbourHQ
      </p>
    </div>
  </section>

  <section class="card card-back" aria-label="Business card back">
    <div class="runner-art" role="img" aria-label="Illustration of a sprinting athlete in layered blue tones"></div>
    <p class="back-tagline">Delivering excellence in sports medicine &amp; athlete care</p>
  </section>

</body>
</html>
```